K5Lesson WebSite

an educational website about tutoring, client will be surfing this site looking for a tutor, please see the attached images because the contains exactly what we need.
Updates

Project Deadline Extended Reason: something went wrong with the uploaded files, we are very sorry.thank you PixelBazaar for the 5 days extension.now there is a 3 images describing the content of the three pages.good luck Added Friday, August 5, 2016

Target Market(s)

everyone

Industry/Entity Type

Education

Number of Pages Required

3 page

Font styles to use
Other font styles liked:
• something looks good in Arabic and english like "Droid Arabic Kufi"

Requirements
Must have
• the logo we attached, responsive design, simple, also try as much as you can Centering texts and layout because this website will have an Arabic version, Arabic is a Right-to-Left Language.
• a change language button,
Nice to have
• educational gestures.
• Centered texts and layout because this website will have an Arabic version, Arabic is a Right-to-Left Language.
• we have a web designer and we can download any template and add our logo and text to it, but.....
• we need creativity, so please stick to the contents in the images we attached, we need something very simple, more like a varnel home page with little touch of filtering fields like the 5 dropdownlist and the gender selection buttons.
• try not to go far away from the contents we specified in the images, use less images or dont use images at all, try not to make the client scroll down,
Should not have
• too much colors or noisy layout or heavy media

```html
<!DOCTYPE html>
<html lang="en">
<head>
<meta charset="utf-8">
<title>K5Lesson – Home</title>
<link href="https://fonts.googleapis.com/css2?family=Open+Sans:wght@400;600;700&family=Roboto:wght@400;500;700&display=swap" rel="stylesheet">
<style>
:root{
  --blue:#1b7fd1;
  --blue-dark:#1565b0;
  --orange:#f08a0e;
  --ink:#333;
  --grey-text:#555;
  --light-bg:#ebebeb;
  --white:#fff;
  --footer:#2a2727;
  --footer-bottom:#1c1a1a;
}
*{box-sizing:border-box;margin:0;padding:0}
html,body{width:748px;height:1200px;overflow:hidden}
body{position:relative;font-family:"Open Sans",Arial,sans-serif;color:var(--ink);background:var(--white)}
.abs{position:absolute}

/* header */
.site-header{left:0;top:0;width:748px;height:70px;background:var(--white);border-top:2px solid var(--orange)}
.brand-name{left:62px;top:20px;font-family:"Open Sans",sans-serif;font-weight:600;font-size:24px;color:var(--ink);letter-spacing:.2px}
.main-nav a{position:absolute;top:31px;font-size:9px;color:var(--ink);text-decoration:none;letter-spacing:.3px;font-family:"Roboto",sans-serif}
.main-nav a.active{color:var(--blue)}
.account-tab{left:536px;top:0;width:148px;height:22px;background:var(--blue);border-radius:0 0 10px 10px;display:flex;font-family:"Roboto",sans-serif;font-size:10px;color:var(--white)}
.account-tab .login{width:58px;background:var(--orange);border-radius:0 0 0 10px;display:flex;align-items:center;justify-content:center;gap:4px}
.account-tab .register{flex:1;display:flex;align-items:center;justify-content:center;gap:4px}
.user-menu{left:553px;top:30px;width:101px;height:88px;background:var(--white);border:1px solid #ddd;border-radius:3px;box-shadow:0 1px 3px rgba(0,0,0,.15);font-size:7.5px;text-align:center;z-index:3}
.user-menu .user{display:flex;align-items:center;gap:6px;padding:5px 6px;border-bottom:1px solid #e5e5e5;font-size:8px;font-weight:600}
.user-menu .avatar{width:18px;height:18px;border-radius:50%;background:#b9c7d3;border:1px solid #8aa}
.user-menu li{list-style:none;padding:4px 0;border-bottom:1px solid #eee}
.user-menu li:last-child{border:0}

/* hero */
.hero{left:0;top:70px;width:748px;height:272px;background:linear-gradient(180deg,#d9d9d9,#c9c9c9)}
.hero-art{left:56px;top:8px;width:304px;height:262px;background:radial-gradient(ellipse at center,#bdbdbd,#cfcfcf 70%);border-radius:8px}
.hero-title{left:330px;top:92px;width:372px;text-align:center;font-family:"Roboto",sans-serif;font-weight:700;font-size:27px;line-height:35px;color:var(--blue)}
.hero-title .accent{color:var(--orange)}
.hero-cta{left:437px;top:172px;width:146px;height:36px;background:var(--blue);color:var(--white);font-family:"Roboto",sans-serif;font-weight:500;font-size:11px;display:flex;align-items:center;justify-content:center;box-shadow:0 3px 5px rgba(0,0,0,.25)}
.slide-arrow{top:126px;width:26px;height:24px;background:#333;display:flex;align-items:center;justify-content:center}

/* category bar */
.category-bar{left:0;top:342px;width:748px;height:32px;background:var(--blue)}
.category-bar span{position:absolute;top:0;height:32px;display:flex;align-items:center;justify-content:center;color:var(--white);font-family:"Roboto",sans-serif;font-weight:700;font-size:10px;border-left:1px solid rgba(255,255,255,.35)}
.category-bar span.last{border-right:1px solid rgba(255,255,255,.35)}

/* about */
.about{left:0;top:374px;width:748px;height:162px;background:var(--light-bg);text-align:center}
.section-title{position:absolute;left:0;width:748px;text-align:center;font-family:"Roboto",sans-serif;font-weight:400;font-size:21px;color:#555;letter-spacing:.5px}
.divider{position:absolute;left:314px;width:120px;height:8px}
.about p{position:absolute;left:72px;top:79px;width:604px;font-size:7.6px;line-height:13px;color:var(--grey-text)}
.read-more{left:347px;top:112px;width:55px;height:17px;background:var(--blue-dark);color:var(--white);font-size:7px;font-weight:700;display:flex;align-items:center;justify-content:center}

/* why band */
.why-band{left:0;top:536px;width:748px;height:238px;background:linear-gradient(180deg,#2f86cf,#2577c0)}
.why-panel{left:74px;top:33px;width:228px;height:139px;background:rgba(236,240,244,.92)}
.why-head{left:68px;top:33px;width:234px;height:25px;background:var(--blue-dark);color:var(--white);font-family:"Roboto",sans-serif;font-weight:700;font-size:11px;display:flex;align-items:center;justify-content:center}
.why-list{left:86px;top:58px;width:204px;list-style:none;text-align:center;font-family:"Roboto",sans-serif;font-weight:500;font-size:9.5px;color:#333}
.why-list li{height:23.2px;line-height:23px;border-bottom:1px solid #bbb}
.why-list li:last-child{border:0}
.why-list li.highlight{color:var(--orange)}
.gender-search{left:74px;top:186px;width:228px;height:20px;background:var(--white);border:1px solid #ccc;display:flex;font-size:7.5px;color:#555}
.gender-search .field{flex:1;display:flex;align-items:center;padding-left:8px}
.gender-search .btn{width:24px;border-left:1px solid #ccc;display:flex;align-items:center;justify-content:center}
.program-photo{left:332px;top:30px;width:354px;height:176px;background:linear-gradient(120deg,#3d6b5e,#7f8a7c 45%,#d9d2c4)}
.program-caption{left:332px;top:146px;width:354px;height:36px;background:rgba(240,240,240,.72);display:flex;align-items:center;justify-content:center;font-family:"Roboto",sans-serif;font-weight:700;font-size:18px;color:var(--orange)}

/* courses */
.courses{left:0;top:774px;width:748px;height:270px;background:var(--light-bg)}
.course{position:absolute;top:78px;width:118px;text-align:center}
.course .photo{width:118px;height:118px}
.course h3{margin:10px auto 0;width:104px;font-family:"Roboto",sans-serif;font-weight:500;font-size:10px;line-height:13px;color:#555}
.course a{display:block;margin-top:2px;font-size:6.5px;color:var(--orange);text-decoration:none}
.round-arrow{top:123px;width:24px;height:24px;border-radius:50%;background:var(--white);border:1px solid #bbb;display:flex;align-items:center;justify-content:center}

/* footer */
.site-footer{left:0;top:1044px;width:748px;height:134px;background:var(--footer);color:#ddd;font-size:7.5px}
.f-head{position:absolute;top:20px;font-family:"Roboto",sans-serif;font-weight:700;font-size:8.5px;color:var(--orange);display:flex;align-items:center;gap:8px}
.f-head::after{content:"";width:30px;height:1px;background:var(--orange)}
.quick-links{position:absolute;left:63px;top:42px;list-style:none}
.quick-links li{height:22.5px}
.contact{position:absolute;left:180px;top:42px;width:140px}
.contact .row{display:flex;gap:8px;margin-bottom:5px;line-height:11px}
.contact .row svg{flex:none;margin-top:1px}
.newsletter{position:absolute;left:360px;top:42px;width:140px}
.newsletter input{display:block;width:140px;height:13px;border:0;margin-top:8px;font-size:6.5px;padding-left:3px;font-family:"Open Sans",sans-serif}
.newsletter .subscribe{margin-top:8px;width:54px;height:16px;background:var(--blue);color:var(--white);font-size:7.5px;font-weight:700;display:flex;align-items:center;justify-content:center}
.col-sep{position:absolute;top:42px;width:1px;height:80px;background:#444}
.footer-brand{position:absolute;left:556px;top:30px;width:130px;text-align:center;font-family:"Open Sans",sans-serif;font-weight:600;font-size:22px;color:#8a8a8a}
.store-badge{position:absolute;left:594px;width:60px;height:16px;border-radius:3px}
.copyright{left:0;top:1178px;width:748px;height:22px;background:var(--footer-bottom);color:#ddd;font-size:7px;display:flex;align-items:center;justify-content:center}
.copyright b{color:var(--orange);font-weight:400}
.social{position:absolute;top:5px;width:12px;height:12px;border:1px solid var(--orange);border-radius:50%}
</style>
</head>
<body>

<header class="abs site-header">
  <div class="abs brand-name">K5Lesson</div>
  <nav class="main-nav">
    <a class="active" style="left:234px">HOME</a>
    <a style="left:289px">FIND A TUTOR</a>
    <a style="left:380px">ABOUT US</a>
    <a style="left:454px">CONTACT US</a>
  </nav>
</header>

<div class="abs account-tab">
  <div class="login">
    <svg width="9" height="9" viewBox="0 0 10 10"><path d="M4 1h5v8H4M1 5h5M4 3l2 2-2 2" fill="none" stroke="#222" stroke-width="1.2"/></svg>Login
  </div>
  <div class="register">
    <svg width="9" height="9" viewBox="0 0 10 10"><circle cx="5" cy="3" r="2.2" fill="#fff"/><path d="M1 10c0-3 2-4 4-4s4 1 4 4z" fill="#fff"/></svg>Register
  </div>
</div>

<div class="abs user-menu">
  <div class="user"><span class="avatar"></span>Sam Carter</div>
  <ul><li>My Profile</li><li>A</li><li>Alerts</li></ul>
</div>

<section class="abs hero">
  <div class="abs hero-art" role="img" aria-label="Student leaping forward surrounded by chalk-style science and math sketches"></div>
  <h1 class="abs hero-title">TAKE THE FIRST STEP TO<br><span class="accent">KNOWLEDGE</span> WITH US</h1>
  <div class="abs hero-cta">Start Learning Now !</div>
  <div class="abs slide-arrow" style="left:0"><svg width="8" height="10" viewBox="0 0 8 10"><path d="M6 1L2 5l4 4" fill="none" stroke="#fff" stroke-width="2"/></svg></div>
  <div class="abs slide-arrow" style="left:722px"><svg width="8" height="10" viewBox="0 0 8 10"><path d="M2 1l4 4-4 4" fill="none" stroke="#fff" stroke-width="2"/></svg></div>
</section>

<nav class="abs category-bar">
  <span style="left:62px;width:84px">ACADEMIC</span>
  <span style="left:146px;width:64px">MUSIC</span>
  <span style="left:210px;width:50px">L.T.</span>
  <span style="left:260px;width:94px">LANGUAGES</span>
  <span style="left:354px;width:83px">BUSINESS</span>
  <span style="left:437px;width:67px">DANCE</span>
  <span style="left:504px;width:73px">SPORTS</span>
  <span class="last" style="left:577px;width:109px">ARTS &amp; CRAFTS</span>
</nav>

<section class="abs about">
  <h2 class="section-title" style="top:26px">ABOUT US</h2>
  <svg class="divider" style="top:59px" viewBox="0 0 120 8"><line x1="0" y1="4" x2="120" y2="4" stroke="#1b7fd1" stroke-width=".8"/><rect x="53" y="0" width="14" height="8" rx="1.5" fill="#1b7fd1"/></svg>
  <p>Lorem ipsum dolor sit amet, consectetuer adipiscing elit, sed diam nonummy nibh euismod tincidunt ut laoreet dolore magna aliquam erat volutpat. Ut wisi enim ad minim veniam, quis nostrud exerci tation ullamcorper suscipit lobortis nisl ut aliquip</p>
  <div class="abs read-more">Read More »</div>
</section>

<section class="abs why-band">
  <div class="abs why-panel"></div>
  <div class="abs why-head">WHY IS K5LESSON IMPORTANT ?</div>
  <ul class="abs why-list">
    <li>Time Management Skills</li>
    <li>Better Organisation</li>
    <li>Reduced Stress</li>
    <li class="highlight">Safe Place To Ask Questions</li>
    <li>Time Savings</li>
  </ul>
  <div class="abs gender-search">
    <div class="field">Male - Female and Both Selection</div>
    <div class="btn"><svg width="10" height="10" viewBox="0 0 10 10"><circle cx="4" cy="4" r="3" fill="none" stroke="#555" stroke-width="1.3"/><path d="M6.3 6.3L9 9" stroke="#555" stroke-width="1.5"/></svg></div>
  </div>
  <div class="abs program-photo" role="img" aria-label="Student reading beside a stack of books"></div>
  <div class="abs program-caption">MASTER &amp; PH D PREPERATION</div>
</section>

<section class="abs courses">
  <h2 class="section-title" style="top:28px">POPULAR COURSES</h2>
  <svg class="divider" style="top:64px;left:274px;width:200px" viewBox="0 0 200 8"><line x1="0" y1="4" x2="200" y2="4" stroke="#1b7fd1" stroke-width=".8"/><rect x="93" y="0" width="14" height="8" rx="1.5" fill="#1b7fd1"/></svg>
  <div class="abs round-arrow" style="left:26px"><svg width="7" height="9" viewBox="0 0 7 9"><path d="M5 1L2 4.5 5 8" fill="none" stroke="#444" stroke-width="1.6"/></svg></div>
  <div class="abs round-arrow" style="left:697px"><svg width="7" height="9" viewBox="0 0 7 9"><path d="M2 1l3 3.5L2 8" fill="none" stroke="#444" stroke-width="1.6"/></svg></div>

  <div class="course" style="left:62px"><div class="photo" role="img" aria-label="Students writing at a desk" style="background:linear-gradient(135deg,#5a5f6b,#c9b7a4)"></div><h3>Spanish for Beginners to Advanced Training</h3><a>View More</a></div>
  <div class="course" style="left:188px"><div class="photo" role="img" aria-label="Smiling student in a library" style="background:linear-gradient(135deg,#7a5a44,#d8c9b8)"></div><h3>Networking for<br>beginners</h3><a>View More</a></div>
  <div class="course" style="left:315px"><div class="photo" role="img" aria-label="Hands on a laptop with code on screen" style="background:linear-gradient(135deg,#b9c9cf,#e9eef0)"></div><h3>Become a Professional Web Designer</h3><a>View More</a></div>
  <div class="course" style="left:441px"><div class="photo" role="img" aria-label="Photographer with a camera in the snow" style="background:linear-gradient(135deg,#f2f2f2,#777)"></div><h3>Your Complete Guide to photography</h3><a>View More</a></div>
  <div class="course" style="left:568px"><div class="photo" role="img" aria-label="Group of students holding books" style="background:linear-gradient(135deg,#c79a6c,#e9ded3)"></div><h3>Medical Chemistry: The Molecular Basis</h3><a>View More</a></div>
</section>

<footer class="abs site-footer">
  <div class="f-head" style="left:62px">Quick Link</div>
  <ul class="quick-links"><li>Home</li><li>Find A Tutor</li><li>About Us</li><li>Contact Us</li></ul>
  <div class="col-sep" style="left:131px"></div>

  <div class="f-head" style="left:180px">Contact Address</div>
  <div class="contact">
    <div class="row"><svg width="8" height="10" viewBox="0 0 8 10"><path d="M4 10S0 5.5 0 3.6A4 4 0 0 1 8 3.6C8 5.5 4 10 4 10z" fill="#fff"/><circle cx="4" cy="3.6" r="1.4" fill="#2a2727"/></svg><div><b style="color:#fff">K5Lesson</b><br>Lorem ipsum dolor sit amet, consectetuer</div></div>
    <div class="row"><svg width="8" height="9" viewBox="0 0 8 9"><rect x="1.5" y="0" width="5" height="9" rx="1" fill="#fff"/></svg>+1.555.010.200</div>
    <div class="row"><svg width="8" height="9" viewBox="0 0 8 9"><rect x="0" y="3" width="8" height="4" fill="#fff"/><rect x="2" y="0" width="4" height="3" fill="#fff"/></svg>+1.555.010.200</div>
    <div class="row"><svg width="8" height="9" viewBox="0 0 8 9"><rect x="0" y="2" width="8" height="6" fill="none" stroke="#fff"/><path d="M0 2l4 3 4-3" fill="none" stroke="#fff"/></svg>info@k5lesson.com</div>
  </div>
  <div class="col-sep" style="left:325px"></div>

  <div class="f-head" style="left:360px">Newsletter Signup</div>
  <div class="newsletter">
    <div style="font-size:6.5px">Signup with us and get update in your inbox.</div>
    <input type="text" value="Your Name">
    <input type="text" value="Email address">
    <div class="subscribe">SUBSCRIBE</div>
  </div>
  <div class="col-sep" style="left:525px"></div>

  <div class="footer-brand">K5Lesson</div>
  <div class="store-badge" style="top:84px;background:#000;border:1px solid #555"></div>
  <div class="store-badge" style="top:104px;background:#9a9a9a"></div>
</footer>

<div class="abs copyright">
  Copyright 2016 by&nbsp;<b>K5Lesson</b>. All Rights Reserved
  <span class="social" style="left:640px"></span>
  <span class="social" style="left:657px"></span>
  <span class="social" style="left:674px"></span>
</div>

</body>
</html>
```